family chiropractic health care team needs a modern business card design

Healthcare office with Chiropractors, Physiotherapists, Massage therapists and possibly other practitioners in the future. This is a friendly family office with patients of all ages (and lots of kids) that just moved into a new larger modern office.
Look at the website for photos of the office.
Design for the front and back of a business card required.
Text for the front:
Office logo and name of the office:
Bright Path Wellness Centre
Name of current Practitioner:
Dr. Marten Quogue B.Sc., D.C. Chiropractor
(But please include options to swap out name and title for other practitioners )

address:
217 Tamsey Road
Etobicoke ON.
K2R 6P4
Phone: 416-870-2961 (MOVE)
Web site and email:
www.brightpathwellcentre.example
brightpathchiro@mailnest.example

2 versions of the back of the card:
1. text below
2. appointment schedule card

Text on back of card:
Chiropractic Card text on back of the card:
There is more to chiropractic than the relief of headaches and back pain! Our primary focus is the integrity of your nerve system, which controls and regulates every cell and tissue of your body. The moving bones of the spinal column can impair this vital communication link between your brain and body. We help improve the function and structure of your spine, reducing nerve system compromise. The result?
Even non-spinal related health problems can show improvement
without drugs
without surgery
regardless of age
for over a century
naturally

Appointment Card info For Back:
Please integrate design elements from the front of the card into an appointment card format.
M Tu W Th F Sat (and a line for writing on beside each one)

```html
<!DOCTYPE html>
<html lang="en">
<head>
<meta charset="utf-8">
<title>Bright Path Wellness Centre – Business Card</title>
<link href="https://fonts.googleapis.com/css2?family=Montserrat:wght@400;500;600;700&display=swap" rel="stylesheet">
<style>
  :root {
    --stage: #141416;
    --card: #1d1d1f;
    --card-edge: #252527;
    --green: #8cc63f;
    --ink: #f2f2f2;
    --muted: #b9b9b9;
    --rule: #8a8a8a;
  }
  * { box-sizing: border-box; margin: 0; padding: 0; }
  html, body { width: 1200px; height: 900px; overflow: hidden; }
  body {
    background: var(--stage);
    font-family: "Montserrat", sans-serif;
    color: var(--ink);
    position: relative;
  }
  .card {
    position: absolute;
    left: 250px;
    width: 700px;
    height: 400px;
    border-radius: 24px;
    background: linear-gradient(160deg, var(--card-edge), var(--card) 55%);
    box-shadow: 0 18px 40px rgba(0,0,0,.55);
    overflow: hidden;
  }
  .card--back { top: 30px; padding: 34px 44px; }
  .card--front { top: 470px; }

  /* Appointment fields */
  .appointment { display: grid; gap: 14px; margin-bottom: 22px; }
  .appointment__row { display: flex; align-items: flex-end; gap: 8px; font-size: 13px; }
  .appointment__label { font-weight: 500; white-space: nowrap; }
  .appointment__line { flex: 1; border-bottom: 1px solid var(--rule); height: 1px; margin-bottom: 4px; }
  .appointment__days { font-size: 12px; color: var(--muted); white-space: nowrap; }

  .about { font-size: 11.5px; line-height: 1.45; color: var(--ink); max-width: 600px; }
  .about__list { list-style: none; margin-top: 2px; font-size: 11.5px; line-height: 1.45; }
  .practitioner { margin-top: 14px; }
  .practitioner__name { color: var(--green); font-weight: 700; font-size: 20px; letter-spacing: .5px; text-transform: uppercase; }
  .practitioner__role { font-size: 13px; color: var(--ink); }

  /* Front */
  .brand {
    position: absolute; top: 62px; right: 60px; width: 360px;
    display: flex; align-items: center; justify-content: center; gap: 12px;
  }
  .brand__dot { width: 18px; height: 18px; border-radius: 50%; background: var(--green); flex: none; }
  .brand__name { color: var(--green); font-weight: 600; font-size: 24px; line-height: 1.2; text-align: center; }

  .doctor { position: absolute; left: 48px; bottom: 58px; }
  .doctor__name { color: var(--green); font-weight: 600; font-size: 26px; }
  .doctor__title { font-size: 15px; margin-top: 4px; padding-left: 150px; }

  .divider { position: absolute; left: 392px; top: 190px; width: 2px; height: 150px; background: var(--green); }

  .contact { position: absolute; left: 414px; top: 190px; font-size: 13.5px; line-height: 1.45; }
  .contact__address { margin-bottom: 12px; }
  .contact__item { display: flex; align-items: center; gap: 10px; }
  .contact__icon { width: 14px; height: 14px; flex: none; }
</style>
</head>
<body>

<section class="card card--back" aria-label="Card back – appointment and chiropractic information">
  <div class="appointment">
    <div class="appointment__row">
      <span class="appointment__label">Name :</span><span class="appointment__line"></span>
      <span class="appointment__days">(M Tu W Th F Sat)</span>
      <span class="appointment__label">Date :</span><span class="appointment__line"></span>
      <span class="appointment__days">(M Tu W Th F Sat)</span>
    </div>
    <div class="appointment__row">
      <span class="appointment__label">Time :</span><span class="appointment__line"></span>
      <span class="appointment__days">(M Tu W Th F Sat)</span>
    </div>
  </div>

  <p class="about">There is more to chiropractic than the relief of headaches and back pain! Our primary focus is the integrity of your nerve system, which controls and regulates every cell and tissue of your body. The moving bones of the spinal column can impair this vital communication link between your brain and body. We help improve the function and structure of your spine, reducing nerve system compromise. The result? Even non-spinal related health problems can show improvement</p>
  <ul class="about__list">
    <li>without drugs</li>
    <li>without surgery</li>
    <li>regardless of age</li>
    <li>for over a century</li>
    <li>naturally</li>
  </ul>

  <div class="practitioner">
    <p class="practitioner__name">Lena Harwick</p>
    <p class="practitioner__role">Cardiologist</p>
  </div>
</section>

<section class="card card--front" aria-label="Card front – practitioner and contact details">
  <div class="brand">
    <span class="brand__dot"></span>
    <span class="brand__name">Bright Path Wellness Centre</span>
  </div>

  <div class="doctor">
    <p class="doctor__name">Dr. Marten Quogue B.Sc</p>
    <p class="doctor__title">D.C. Chiropractor</p>
  </div>

  <span class="divider"></span>

  <div class="contact">
    <p class="contact__address">217 Tamsey Road<br>Etobicoke ON.<br>K2R 6P4</p>
    <p class="contact__item">
      <svg class="contact__icon" viewBox="0 0 16 16" aria-hidden="true"><path fill="#8cc63f" d="M3.5 1.5l2.5 0 1 3.5-1.6 1.2a9 9 0 0 0 4.4 4.4L11 9l3.5 1v2.5a2 2 0 0 1-2 2A11 11 0 0 1 1.5 3.5a2 2 0 0 1 2-2z"/></svg>
      416-870-2961 (MOVE)
    </p>
    <p class="contact__item">
      <svg class="contact__icon" viewBox="0 0 16 16" aria-hidden="true"><rect x="1" y="3" width="14" height="10" rx="1.5" fill="#8cc63f"/><path d="M1.5 4l6.5 5 6.5-5" stroke="#1d1d1f" stroke-width="1.4" fill="none"/></svg>
      brightpathchiro@mailnest.example
    </p>
    <p class="contact__item">
      <svg class="contact__icon" viewBox="0 0 16 16" aria-hidden="true"><circle cx="8" cy="8" r="6.5" fill="none" stroke="#8cc63f" stroke-width="1.5"/><path d="M1.5 8h13M8 1.5c-3 3.5-3 9.5 0 13M8 1.5c3 3.5 3 9.5 0 13" stroke="#8cc63f" stroke-width="1.2" fill="none"/></svg>
      www.brightpathwellcentre.example
    </p>
  </div>
</section>

</body>
</html>
```